Kestowell Chardonnay Wine Label 2024

We need a wine label design for a small, family-owned vineyard in Broke, Hunter Valley of NSW (Australia). The vineyard is called Kestowell and we have an existing logo and 'brand book' for the vineyard home that is rented out for short stay bookings. This is attached and includes font style, colour palette and our Kestowell logo for the accommodation (we're not wedded to this but also probably not after a completely different rethink either as we want the accommodation and the wine to feel part of the same thing.

Project:
The initial label requirement (front and back) is for the Kestowell 2024 Chardonnay, which is called 'Marigold'. The label would need to be able to extend to other varietals (eg Verdehlo and Sparkling) in 2025. Attached is draft copy for front and back for the 2024 Chardonnay as a guide.

STYLE: We like a relatively simple, classic design and have played with both a dark (navy) and a light background (white/cream). Based on the final label design we will order a Tarquo colour to pick up on the label theme.

The Chardonnay bottle dimensions are attached, as is our logo file (if that helps)

Target Market(s)

online 25-50 yearold

Industry/Entity Type

Wine

Requirements
Must have
• front and back label design Kestowell logo and name

```html
<!DOCTYPE html>
<html lang="en">
<head>
<meta charset="utf-8">
<title>Kestowell Marigold Chardonnay 2024 – Front Label</title>
<link rel="stylesheet" href="https://fonts.googleapis.com/css2?family=Bodoni+Moda:wght@500&family=Literata:wght@500&family=Montserrat:wght@300;400&display=swap">
<style>
  :root {
    --navy: #0f1a2e;
    --navy-soft: #6f7787;
    --navy-pale: #c9ccd3;
    --paper: #ffffff;
  }
  * { box-sizing: border-box; margin: 0; padding: 0; }
  html, body {
    width: 801px;
    height: 1200px;
    overflow: hidden;
    background: var(--paper);
  }
  .label {
    position: relative;
    width: 801px;
    height: 1200px;
    background: var(--paper);
    color: var(--navy);
  }
  .top-border {
    position: absolute;
    left: 0;
    top: 28px;
    width: 801px;
    height: 96px;
  }
  .brand {
    position: absolute;
    top: 262px;
    left: 233px;
    font-family: "Literata", Georgia, serif;
    font-weight: 500;
    font-size: 61px;
    letter-spacing: 0.5px;
    line-height: 1;
    white-space: nowrap;
    color: var(--navy);
  }
  .brand-mark {
    position: absolute;
    left: 478px;
    top: 184px;
    width: 78px;
    height: 78px;
    border-radius: 50%;
    background: var(--navy);
  }
  .wine-name {
    position: absolute;
    top: 394px;
    left: 0;
    width: 801px;
    text-align: center;
    font-family: "Bodoni Moda", "Times New Roman", serif;
    font-weight: 500;
    font-size: 124px;
    letter-spacing: 0;
    line-height: 1;
    white-space: nowrap;
    color: var(--navy);
  }
  .varietal {
    position: absolute;
    top: 518px;
    left: 0;
    width: 801px;
    text-align: center;
    font-family: "Montserrat", Arial, sans-serif;
    font-weight: 300;
    font-size: 44px;
    letter-spacing: 1px;
    line-height: 1;
    color: var(--navy);
  }
  .region-illustration {
    position: absolute;
    left: 154px;
    top: 612px;
    width: 493px;
    height: 410px;
  }
  .volume {
    position: absolute;
    top: 1049px;
    left: 0;
    width: 801px;
    text-align: center;
    font-family: "Montserrat", Arial, sans-serif;
    font-weight: 400;
    font-size: 36px;
    line-height: 1;
    color: var(--navy);
  }
  .base-band {
    position: absolute;
    left: 0;
    top: 1153px;
    width: 801px;
    height: 21px;
    background: var(--navy);
  }
</style>
</head>
<body>
  <main class="label">
    <svg class="top-border" viewBox="0 0 801 96">
      <line x1="0" y1="2" x2="801" y2="2" stroke="var(--navy)" stroke-width="3"/>
      <line x1="0" y1="94" x2="801" y2="94" stroke="var(--navy)" stroke-width="3"/>
      <rect role="img" aria-label="Decorative floral border band" x="0" y="14" width="801" height="68" fill="var(--navy-pale)"/>
    </svg>

    <div class="brand-mark" aria-hidden="true"></div>
    <h1 class="brand">Kestowell</h1>

    <h2 class="wine-name">MARIGOLD</h2>

    <p class="varietal">Chardonnay 2024</p>

    <svg class="region-illustration" viewBox="0 0 493 410" role="img"
         aria-label="Engraved Hunter Valley vineyard scene with rolling hills, a bird in flight before the sun, wagons and rows of vines framed by a banner">
      <defs>
        <radialGradient id="scene-tone" cx="50%" cy="45%" r="60%">
          <stop offset="0%" stop-color="var(--navy-pale)"/>
          <stop offset="100%" stop-color="var(--navy-soft)"/>
        </radialGradient>
      </defs>
      <path d="M40 60 Q246 -20 453 60 L493 330 Q246 430 0 330 Z" fill="url(#scene-tone)"/>
    </svg>

    <p class="volume">750ml</p>

    <div class="base-band"></div>
  </main>
</body>
</html>
```